HARBOR VALE Insurance Business Card Design

We need a business card designed for our personal risk / life insurance business based in Sydney Australia called 'Harbor Vale'.

We manage and implement life insurance policies for individuals, businesses and families. Work on estate planning and succession planning. We help individuals make sure that they will be covered financially in the event of disability or critical illness.

We would like to see designs that use the colours Black, Silver/Grey , White OR different shades of Blue that are suitable for the finance / professional industries.

The final design should communicate financial safety and can also feel contemporary.

Hello,

Thanks for submitting your design.
We have recieved MANY great new designs today, thank-you.
Sorry for the late notice but for legal reasons we must include additional information of the card as follows:

Level 5, Suite 5.31,
47 Wattlebark Lane
MORWENTON NSW 2098

Authorised Representative No. 493172
Tallowmere Wealth Partners Pty Ltd
ABN 47 218 664 905
AFS Licence No. 582904

PLEASE REMOVE:
S marcuspellworth

PLEASE ADD:
www.harborvale-example.com.au

Industry/Entity Type

Life Insurance

Contact Information for Business Card

Marcus Pellworth
Senior Advisor
Managing Director

M +61400 587 294
E Marcus@harborvale-example.com.au
S marcuspellworth

Level 5, Suite 5.31
47 Wattlebark Lane
MORWENTON NSW 2098

Font styles to use
Serif
Sans Serif

Requirements
Must have
• - LANDSCAPE design

- MUST BE DOUBLE SIDED

Level 5, Suite 5.31,
47 Wattlebark Lane
MORWENTON NSW 2098

ABN 47 218 664 905
AFS Licence No. 582904

PLEASE REMOVE:
S marcuspellworth

PLEASE ADD:
www.harborvale-example.com.au
Nice to have
• - Can have a rounded corner... but doesn't have to

```html
<!DOCTYPE html>
<html lang="en">
<head>
<meta charset="utf-8">
<title>Harbor Vale – Business Card Designs</title>
<link rel="stylesheet" href="https://fonts.googleapis.com/css2?family=Cinzel:wght@500&family=Source+Sans+3:wght@400;600;700&display=swap">
<style>
  :root {
    --ink: #1a1a1a;
    --band: #0d0d0d;
    --blue: #3b9cc4;
    --blue-light: #6cc4e4;
    --plate: #5f6062;
    --mark: #3a3a3c;
    --mark-faint: #a9abae;
    --mark-ghost: #d9d9da;
    --label: #222222;
    --paper: #ffffff;
    --serif: "Cinzel", "Times New Roman", serif;
    --sans: "Source Sans 3", "Helvetica Neue", Arial, sans-serif;
  }
  * { box-sizing: border-box; margin: 0; padding: 0; }
  html, body { width: 1200px; height: 915px; overflow: hidden; background: var(--paper); }
  .sheet { position: relative; width: 1200px; height: 915px; font-family: var(--sans); color: var(--label); }

  .design-title { position: absolute; top: 40px; font-size: 21px; width: 300px; text-align: center; }
  .design-title--one { left: 150px; }
  .design-title--two { left: 703px; }
  .side-label { position: absolute; font-size: 19px; }

  .card { position: absolute; width: 500px; height: 310px; overflow: hidden; background: var(--paper);
          box-shadow: 0 1px 4px rgba(0,0,0,.25); }
  .card svg.card-shapes { position: absolute; inset: 0; width: 100%; height: 100%; }
  .card--one-front { left: 56px; top: 146px; }
  .card--two-front { left: 639px; top: 146px; }
  .card--one-back  { left: 56px; top: 548px; }
  .card--two-back  { left: 639px; top: 548px; }

  .wordmark { position: absolute; display: flex; align-items: center; gap: 12px;
              font-family: var(--serif); font-weight: 500; white-space: nowrap; }
  .wordmark__square { display: block; background: currentColor; }

  .card--one-front .wordmark { left: 42px; top: 34px; font-size: 44px; color: var(--mark); }
  .card--one-front .wordmark__square { width: 62px; height: 62px; }
  .card--two-front .wordmark { left: 34px; top: 36px; font-size: 31px; color: var(--mark); gap: 10px; }
  .card--two-front .wordmark__square { width: 44px; height: 44px; }

  .person { position: absolute; text-align: right; white-space: nowrap; }
  .person__name { font-weight: 700; line-height: 1; }
  .person__role { font-size: 10px; line-height: 1.3; }
  .card--one-front .person { right: 18px; top: 128px; color: #fff; }
  .card--one-front .person__name { font-size: 22px; }
  .card--two-front .person { right: 16px; top: 100px; color: var(--ink); }
  .card--two-front .person__name { font-size: 22px; }

  .contact { position: absolute; font-size: 14.5px; line-height: 1.75; white-space: nowrap; }
  .card--one-front .contact { left: 104px; top: 210px; color: #fff; }
  .card--two-front .contact { right: 16px; top: 140px; color: var(--ink); font-size: 13px; line-height: 1.34; }
  .contact__legal { font-size: 10.5px; }

  .photo-area { position: absolute; left: 0; top: 26px; width: 500px; height: 200px;
                background: linear-gradient(180deg, #c9ced4 0%, #dfe2e6 55%, #ffffff 100%); }
  .card--one-back .wordmark { left: 88px; top: 196px; font-size: 40px; color: var(--mark-faint); }
  .card--one-back .wordmark__square { width: 56px; height: 56px; }
  .card--two-back .wordmark { left: 14px; top: 72px; font-size: 58px; color: var(--mark-ghost); }
</style>
</head>
<body>
<main class="sheet">
  <div class="design-title design-title--one">Design 1</div>
  <div class="design-title design-title--two">Design 2</div>

  <div class="side-label" style="left:75px;top:104px">Front</div>
  <div class="side-label" style="left:669px;top:104px">Front</div>
  <div class="side-label" style="left:75px;top:506px">Back</div>
  <div class="side-label" style="left:669px;top:506px">Back</div>

  <!-- Design 1 front -->
  <section class="card card--one-front">
    <svg class="card-shapes" viewBox="0 0 500 310" aria-hidden="true">
      <rect x="0" y="0" width="500" height="26" fill="var(--band)"/>
      <rect x="0" y="188" width="500" height="122" fill="var(--blue)"/>
      <polygon points="232,188 272,118 500,118 500,188" fill="var(--plate)"/>
      <polygon points="46,187 96,187 71,225" fill="var(--paper)"/>
    </svg>
    <div class="wordmark"><span class="wordmark__square"></span>HARBOR VALE</div>
    <div class="person">
      <div class="person__name">Marcus Pellworth</div>
      <div class="person__role">Senior Advisor Managing Director</div>
    </div>
    <div class="contact">
      Mobile: +61400 587 294 &nbsp; Level 5, Suite 5.31,<br>
      47 Wattlebark Lane<br>
      MORWENTON NSW 2098 • Marcus@harborvale-example.com.au
    </div>
  </section>

  <!-- Design 2 front -->
  <section class="card card--two-front">
    <svg class="card-shapes" viewBox="0 0 500 310" aria-hidden="true">
      <defs>
        <linearGradient id="blueFace" x1="0" y1="0" x2="1" y2="1">
          <stop offset="0" stop-color="var(--blue)"/>
          <stop offset="1" stop-color="var(--blue-light)"/>
        </linearGradient>
      </defs>
      <rect x="0" y="0" width="500" height="24" fill="var(--band)"/>
      <polygon points="0,24 340,24 296,112 0,112" fill="url(#blueFace)"/>
      <polygon points="0,112 296,112 196,310 0,310" fill="var(--band)"/>
      <rect x="205" y="280" width="135" height="4" fill="var(--band)"/>
      <rect x="340" y="280" width="160" height="4" fill="var(--blue)"/>
    </svg>
    <div class="wordmark"><span class="wordmark__square"></span>HARBOR VALE</div>
    <div class="person">
      <div class="person__name">Marcus Pellworth</div>
      <div class="person__role">Senior Advisor Managing Director</div>
    </div>
    <div class="contact">
      Mobile: +61400 587 294<br>
      Level 5, Suite 5.31,<br>
      47 Wattlebark Lane<br>
      MORWENTON NSW 2098<br>
      Marcus@harborvale-example.com.au<br>
      www.harborvale-example.com.au<br>
      <span class="contact__legal">ABN 47 218 664 905 • AFS Licence No. 582904</span>
    </div>
  </section>

  <!-- Design 1 back -->
  <section class="card card--one-back">
    <div class="photo-area" role="img" aria-label="Faded photograph of a calculator and pen on financial papers"></div>
    <svg class="card-shapes" viewBox="0 0 500 310" aria-hidden="true">
      <rect x="0" y="0" width="500" height="26" fill="var(--band)"/>
    </svg>
    <div class="wordmark"><span class="wordmark__square"></span>HARBOR VALE</div>
  </section>

  <!-- Design 2 back -->
  <section class="card card--two-back">
    <svg class="card-shapes" viewBox="0 0 500 310" aria-hidden="true">
      <rect x="0" y="0" width="500" height="24" fill="var(--band)"/>
    </svg>
    <div class="wordmark">HARBOR VALE</div>
  </section>
</main>
</body>
</html>
```